The Harlow Law Firm, PC

Dwight K. Harlow
Attorney at Law
physical address: 287 E. 9th Avenue
Greenville, NC 27019

mailing: P.O. Box 5843
Greenville, NC 27021

o. 555.416.2071
f. 555.416.8532

www.harlowlegal-ex.com

Industry/Entity Type

Attorney

Contact Information for Business Card

Attorney name
Office Phone number
Office Fax number
Mailing address and physical address
website address

Requirements
Must have
• Clean fresh design - I hate the website

```html
<!DOCTYPE html>
<html lang="en">
<head>
<meta charset="utf-8">
<title>The Harlow Law Firm, PC — Business Card</title>
<link rel="stylesheet" href="https://fonts.googleapis.com/css2?family=Source+Sans+3:wght@400;600&display=swap">
<style>
  :root {
    --backdrop: #4a4a4a;
    --card: #fbfbfb;
    --navy: #0d3a84;
    --name-blue: #1c3f86;
    --ink: #555555;
    --muted: #8c8c8c;
    --rule: #a9a9a9;
    --steel: #7a7a7a;
  }
  * { margin: 0; padding: 0; box-sizing: border-box; }
  html, body {
    width: 1200px; height: 849px; overflow: hidden;
    background: var(--backdrop);
    font-family: "Source Sans 3", "Myriad Pro", Arial, sans-serif;
  }
  .card {
    position: absolute; left: 100px; top: 139px;
    width: 1000px; height: 571px;
    background: var(--card);
    overflow: hidden;
  }
  .firm-name {
    position: absolute; right: 68px; top: 64px;
    text-align: right; color: var(--navy);
    font-weight: 600; text-transform: uppercase;
    line-height: 1;
  }
  .firm-name .primary { display: block; font-size: 58px; letter-spacing: 1px; }
  .firm-name .secondary { display: block; font-size: 40px; margin-top: 6px; letter-spacing: 0.5px; }
  .attorney-name {
    position: absolute; left: 53px; top: 280px;
    font-size: 36px; font-weight: 600; color: var(--name-blue);
  }
  .title-line {
    position: absolute; left: 55px; top: 333px; width: 876px;
    display: flex; align-items: center; gap: 6px;
    font-size: 26px; color: var(--muted);
  }
  .title-line::after {
    content: ""; flex: 1; height: 2px; background: var(--rule);
  }
  .contact {
    position: absolute; top: 390px; font-size: 25px; line-height: 34px; color: var(--ink);
  }
  .contact .label { font-weight: 600; }
  .physical { left: 55px; }
  .mailing { left: 390px; }
  .divider { position: absolute; top: 398px; width: 2px; height: 88px; background: var(--rule); }
  .divider.first { left: 345px; }
  .divider.second { left: 680px; }
  .phones { position: absolute; left: 733px; top: 410px; font-size: 25px; color: var(--ink); }
  .phones li { list-style: none; display: flex; align-items: center; gap: 14px; height: 39px; }
  .phones svg { width: 30px; height: 26px; fill: var(--navy); }
  .bands { position: absolute; left: 0; bottom: 0; width: 1000px; height: 38px; }
</style>
</head>
<body>
  <div class="card">
    <div class="firm-name"><span class="primary">The Harlow</span><span class="secondary">Law Firm, PC</span></div>

    <div class="attorney-name">Dwight K. Harlow</div>
    <div class="title-line">Attorney at Law</div>

    <div class="contact physical">
      <div class="label">Physical Address:</div>
      <div>287 E. 9th Avenue</div>
      <div>Greenville, NC 27019</div>
    </div>
    <span class="divider first"></span>
    <div class="contact mailing">
      <div class="label">Mailing Address:</div>
      <div>P.O. Box 5843</div>
      <div>Greenville, NC 27021</div>
    </div>
    <span class="divider second"></span>

    <ul class="phones">
      <li>
        <svg viewBox="0 0 30 26" aria-label="Phone"><path d="M2 9c0-5 26-5 26 0v3h-6V9c-3-1-11-1-14 0v3H2z"/><path d="M7 12h16l4 12H3z M11 15a4 4 0 1 0 8 0a4 4 0 1 0-8 0" fill-rule="evenodd"/></svg>
        <span>555.416.2071</span>
      </li>
      <li>
        <svg viewBox="0 0 30 26" aria-label="Fax"><path d="M8 2h14v7H8z"/><path d="M3 10h24v10h-4v-4H7v4H3z"/><path d="M8 17h14v7H8z"/></svg>
        <span>555.416.8532</span>
      </li>
    </ul>

    <svg class="bands" viewBox="0 0 1000 38" preserveAspectRatio="none" aria-hidden="true">
      <polygon points="0,0 643,0 633,38 0,38" fill="var(--navy)"/>
      <polygon points="653,0 1000,0 1000,38 643,38" fill="var(--steel)"/>
    </svg>
  </div>
</body>
</html>
```